Presentation Folder

We want to create a clean, modern folder for our three companies- A single folder. Feel free to be as creative as possible. We are good with some color, but want it to stay clean and modern. See our website lumivantpartners.com for more idea of the vibe. I've attached all 3 logos to be used as well as our new business cards

Target Market(s)

Senior executives

Industry/Entity Type

Business

Font styles to use
Serif
Sans Serif

Colors
85acd3
3176b5
0455a3
0792cd
34a6d7
85cae6

Requirements
Must have
• All 3 logos websites and phone numbers (see business card).

```html
<!DOCTYPE html>
<html lang="en">
<head>
<meta charset="utf-8">
<title>Presentation Folder – Corvane, Keystone, Lumivant</title>
<link rel="stylesheet" href="https://fonts.googleapis.com/css2?family=Lato:wght@400;700&family=Roboto+Slab:wght@700&display=swap">
<style>
  :root {
    --ink-dark: #3b3b3c;
    --ink-mid: #5e5e60;
    --ink-soft: #6f6e6e;
    --sky: #7fc4e0;
    --sky-deep: #66a6c0;
    --sky-cover: #6eafca;
    --orange: #f0961e;
    --paper: #ffffff;
    --stage-top: #e4e4e4;
    --stage-bottom: #c2c2c2;
    --label: #e9e9e9;
  }
  html, body { margin: 0; padding: 0; overflow: hidden; }
  body { width: 1200px; height: 1192px; background: var(--stage-bottom); }
  .canvas { display: block; width: 1200px; height: 1192px; }
  .brand { font-family: "Lato", sans-serif; font-weight: 700; fill: var(--label); }
  .brand-light { font-family: "Lato", sans-serif; font-weight: 400; fill: var(--label); }
  .brand-slab { font-family: "Roboto Slab", serif; font-weight: 700; fill: var(--label); }
  .card-text { font-family: "Lato", sans-serif; font-weight: 400; }
  .giant { font-family: "Lato", sans-serif; font-weight: 700; fill: var(--paper); }
</style>
</head>
<body>
<svg class="canvas" viewBox="0 0 1200 1192" xmlns="http://www.w3.org/2000/svg">
  <defs>
    <linearGradient id="stage" x1="0" y1="0" x2="0" y2="1">
      <stop offset="0" stop-color="var(--stage-top)"/>
      <stop offset="1" stop-color="var(--stage-bottom)"/>
    </linearGradient>
    <clipPath id="top-band-clip"><rect width="1200" height="183"/></clipPath>
    <clipPath id="bottom-band-clip"><rect y="1008" width="1200" height="184"/></clipPath>
    <clipPath id="cover-clip"><rect x="80" y="300" width="308" height="600"/></clipPath>
    <clipPath id="disc-clip"><rect x="600" y="640" width="220" height="130"/></clipPath>
  </defs>

  <!-- Top brand band -->
  <g class="band-top" clip-path="url(#top-band-clip)">
    <rect width="1200" height="183" fill="var(--ink-soft)"/>
    <polygon points="195,0 1200,0 1200,40 1100,183 237,183" fill="var(--ink-dark)"/>
    <polygon points="1010,0 1200,0 1200,36" fill="var(--orange)"/>
    <polygon points="1200,40 1200,183 1100,183" fill="var(--sky)"/>
    <g transform="rotate(7 600 90)">
      <text class="brand" x="250" y="28" font-size="44">CORVANE</text>
      <text class="brand-light" x="250" y="62" font-size="28">ASSOCIATES</text>
      <text class="brand-light" x="600" y="16" font-size="20">THE</text>
      <text class="brand-slab" x="548" y="60" font-size="40">KEYSTONE</text>
      <text class="brand-light" x="550" y="94" font-size="22" letter-spacing="5">ACADEMY</text>
      <rect x="790" y="80" width="16" height="16" fill="var(--label)"/>
      <text class="brand" x="816" y="100" font-size="46">LUMIVANT</text>
      <text class="brand-light" x="900" y="128" font-size="16" letter-spacing="12">SEARCH</text>
    </g>
  </g>

  <!-- Stage -->
  <rect y="183" width="1200" height="825" fill="url(#stage)"/>

  <!-- Folder front cover -->
  <g class="folder-cover" clip-path="url(#cover-clip)">
    <rect x="80" y="300" width="308" height="600" fill="var(--ink-mid)"/>
    <polygon points="80,604 388,496 388,900 80,900" fill="var(--ink-dark)"/>
    <polygon points="80,690 388,780 388,900 80,900" fill="var(--sky-cover)"/>
    <rect x="150" y="395" width="28" height="28" fill="var(--label)" transform="rotate(45 164 409)"/>
    <text class="brand" x="97" y="493" font-size="32">CORVANE</text>
    <text class="brand-light" x="97" y="517" font-size="20">ASSOCIATES</text>
    <text class="brand-light" x="372" y="612" font-size="20" text-anchor="end">THE</text>
    <text class="brand-slab" x="252" y="668" font-size="28" textLength="120" lengthAdjust="spacingAndGlyphs">KEYSTONE</text>
    <text class="brand-light" x="253" y="710" font-size="19" letter-spacing="2" textLength="119">ACADEMY</text>
    <text class="brand" x="118" y="818" font-size="36">LUMIVANT</text>
    <text class="brand-light" x="156" y="841" font-size="12" letter-spacing="10">SEARCH</text>
  </g>

  <!-- Folder inside spread -->
  <g class="folder-inside">
    <rect x="555" y="335" width="290" height="535" fill="var(--sky)"/>
    <rect x="845" y="335" width="292" height="535" fill="var(--sky-deep)"/>

    <g class="disc" clip-path="url(#disc-clip)">
      <circle cx="706" cy="742" r="85" fill="var(--ink-mid)"/>
      <path d="M621,742 A85,85 0 0 1 791,742 Z" fill="var(--orange)"/>
      <polygon points="640,686 772,686 706,760" fill="var(--ink-dark)"/>
      <text class="brand" x="674" y="706" font-size="5" text-anchor="middle" textLength="26" lengthAdjust="spacingAndGlyphs">CORVANE</text>
      <text class="brand-light" x="674" y="712" font-size="3.5" text-anchor="middle">ASSOCIATES</text>
      <text class="brand" x="706" y="705" font-size="5" text-anchor="middle" textLength="24" lengthAdjust="spacingAndGlyphs">KEYSTONE</text>
      <text class="brand-light" x="706" y="711" font-size="3.5" text-anchor="middle">ACADEMY</text>
      <text class="brand" x="740" y="702" font-size="5" text-anchor="middle" textLength="26" lengthAdjust="spacingAndGlyphs">LUMIVANT</text>
      <text class="brand-light" x="740" y="708" font-size="3.5" text-anchor="middle">SEARCH</text>
      <circle cx="706" cy="742" r="20" fill="#9a9a9a"/>
      <circle cx="706" cy="742" r="8" fill="var(--ink-dark)"/>
    </g>

    <polygon points="555,720 625,720 630,768 790,768 790,708 840,708 840,870 555,870" fill="var(--ink-dark)"/>
    <rect x="849" y="707" width="288" height="163" fill="var(--ink-soft)"/>

    <g class="business-card">
      <rect x="920" y="742" width="126" height="84" fill="var(--paper)"/>
      <rect x="920" y="815" width="126" height="11" fill="var(--sky)"/>
      <text class="card-text" x="983" y="779" font-size="11" text-anchor="middle" fill="#333">DANIEL HART</text>
      <text class="card-text" x="983" y="791" font-size="7" text-anchor="middle" fill="#888">CEO</text>
      <text class="card-text" x="983" y="823" font-size="5.5" text-anchor="middle" fill="#3a6f85">daniel@lumivantpartners.com</text>
    </g>
  </g>

  <!-- Bottom brand band -->
  <g class="band-bottom" clip-path="url(#bottom-band-clip)">
    <rect y="1008" width="1200" height="184" fill="var(--ink-soft)"/>
    <g transform="rotate(-8 450 1150)">
      <text class="giant" x="40" y="1200" font-size="210">CORVANE</text>
      <text class="giant" x="180" y="1340" font-size="150" style="font-weight:400">ASSOCIATES</text>
    </g>
  </g>
</svg>
</body>
</html>
```